Customer Upgrade from Free to Paid Investment Management

Our intent is to have customers that use our free online service consider converting into our paid investment management service.

In current vernacular, we have a Freemium business proposition - but we are just at the early stages of building out our upgrade capabilities.

The design request is detailed in the attached file, but essentially, I'm looking to add another banner to our library. Let me see what you can do!

Target Market(s)

40s-50s, can have any balance in their 401k, at first thought they could manage their 401k themselves, but may be interested in having us manage.

Industry/Entity Type

Investment

Requirements
Must have
• Keep it very simple.
Banner specs are attached in the file
Should not have
• No animation
No "hard sell"

```html
<!DOCTYPE html>
<html lang="en">
<head>
<meta charset="UTF-8">
<title>Upgrade Banners</title>
<link href="https://fonts.googleapis.com/css2?family=Arimo:wght@400;700&display=swap" rel="stylesheet">
<style>
  :root {
    --page-bg: #ffffff;
    --headline: #f47a20;
    --subline-grey: #4a4a4a;
    --border: #dcdcdc;
    --blue-top: #63b8ef;
    --blue-mid: #cde8fa;
    --blue-bottom: #ffffff;
    --green-top: #bde9a0;
    --green-bottom: #eefbe4;
    --btn-blue-top: #6cc0f5;
    --btn-blue-bottom: #2a8ad8;
    --btn-blue-edge: #1a5c9c;
    --btn-green-top: #86c95a;
    --btn-green-bottom: #4a952c;
    --btn-green-edge: #3a7a22;
    --btn-text: #1d2b36;
    --photo-top: #c9cdd1;
    --photo-bottom: #8f8a85;
  }
  * { box-sizing: border-box; margin: 0; padding: 0; }
  html, body {
    width: 1200px; height: 640px; overflow: hidden;
    background: var(--page-bg);
    font-family: "Arimo", Arial, sans-serif;
  }
  .canvas { position: relative; width: 1200px; height: 640px; }

  .banner {
    position: absolute; left: 91px; width: 1004px; height: 117px;
    border: 1px solid var(--border); border-radius: 8px;
  }
  .banner--help { top: 156px; background: linear-gradient(to bottom, var(--blue-top), var(--blue-mid) 55%, var(--blue-bottom)); }
  .banner--charge { top: 358px; background: linear-gradient(to bottom, var(--green-top), var(--green-bottom)); }

  .advisor-photo {
    position: absolute; left: 12px; bottom: 0; width: 124px; height: 141px;
    border-radius: 60px 60px 0 0;
    background: linear-gradient(to bottom, var(--photo-top), var(--photo-bottom));
  }

  .message { position: absolute; left: 144px; }
  .banner--help .message { top: 27px; }
  .banner--charge .message { top: 26px; }
  .headline { font-size: 28px; font-weight: 700; color: var(--headline); line-height: 1.1; }
  .subline { margin-top: 7px; font-size: 18px; color: var(--subline-grey); }
  .subline--accent { margin-top: 5px; font-size: 26px; color: var(--headline); }

  .learn-more {
    position: absolute; display: block; text-decoration: none;
    font-weight: 700; color: var(--btn-text); font-size: 16px;
  }
  .learn-more--tag { left: 808px; top: 36px; width: 172px; height: 51px; }
  .learn-more--tag svg { position: absolute; inset: 0; }
  .learn-more--tag span { position: absolute; left: 38px; top: 15px; }

  .learn-more--pill {
    left: 862px; top: 35px; width: 130px; height: 44px;
    border: 1px solid var(--btn-green-edge); border-radius: 4px;
    background: linear-gradient(to bottom, var(--btn-green-top), var(--btn-green-bottom));
    box-shadow: 0 6px 8px -3px rgba(0,0,0,0.35);
    font-size: 15px; text-align: center; line-height: 42px;
  }
</style>
</head>
<body>
<main class="canvas">
  <section class="banner banner--help">
    <div class="advisor-photo" role="img" aria-label="Portrait photo of a smiling grey-haired woman"></div>
    <div class="message">
      <h2 class="headline">It's ok if you don't know what to do next.</h2>
      <p class="subline">Not sure what to do from here?</p>
    </div>
    <a class="learn-more learn-more--tag" href="#">
      <svg width="172" height="51" viewBox="0 0 172 51" aria-hidden="true">
        <defs>
          <linearGradient id="tagFill" x1="0" y1="0" x2="0" y2="1">
            <stop offset="0" stop-color="#6cc0f5"/>
            <stop offset="1" stop-color="#2a8ad8"/>
          </linearGradient>
        </defs>
        <path d="M1 25.5 L22 1 H166 a5 5 0 0 1 5 5 V45 a5 5 0 0 1 -5 5 H22 Z" fill="url(#tagFill)" stroke="#1a5c9c" stroke-width="1.5"/>
      </svg>
      <span>Learn More &raquo;</span>
    </a>
  </section>

  <section class="banner banner--charge">
    <div class="advisor-photo" role="img" aria-label="Portrait photo of a smiling grey-haired woman"></div>
    <div class="message">
      <h2 class="headline">You are in charge, we can do the work.</h2>
      <p class="subline subline--accent">Taking care of this can be painless.</p>
    </div>
    <a class="learn-more learn-more--pill" href="#">Learn More &raquo;</a>
  </section>
</main>
</body>
</html>
```